Diesel Fitting/Mechanical Company Needs a new Business Card

We would like a new business card that showcases our logo and business information.

Industry/Entity Type

Business

Contact Information for Business Card

314 Wendale Street
PO Box 7581 BRAMWELL FLATS QLD 4825
Phone: 49312787 Fax: 49312688 Mobile: 0438915276 ABN: 63 519 087 342

Requirements
Must have
• The following email addresses:
• admin@tkservicing.com.au , sales@tkservicing.com.au , accounts@tkservicing.com.au , parts@tkservicing.com.au , office@tkservicing.com.au
• Also need to have the website: www.tkservicing.com.au

```html
<!DOCTYPE html>
<html lang="en">
<head>
<meta charset="utf-8">
<title>TK Servicing – Business Card</title>
<link rel="stylesheet" href="https://fonts.googleapis.com/css2?family=Poppins:wght@600&family=Questrial&display=swap">
<style>
  :root {
    --backdrop: #e4e1dc;
    --card-black: #0b0b0b;
    --card-white: #ffffff;
    --accent-red: #e5232b;
    --accent-orange: #f47920;
    --text-light: #ffffff;
    --mark-grey: #c9c9c9;
  }
  * { margin: 0; padding: 0; box-sizing: border-box; }
  html, body { width: 1000px; height: 1200px; overflow: hidden; }
  body {
    background: var(--backdrop);
    position: relative;
    font-family: "Questrial", "Century Gothic", sans-serif;
  }
  .card {
    position: absolute;
    left: 108px;
    width: 787px;
    height: 460px;
    box-shadow: 0 3px 10px rgba(0,0,0,0.35);
    overflow: hidden;
  }
  .card-front { top: 112px; background: var(--card-black); color: var(--text-light); }
  .card-back { top: 623px; width: 785px; background: var(--card-white); }

  .corner-accent, .web-band { position: absolute; }
  .corner-accent { top: 0; right: 0; }
  .web-band { left: 0; bottom: 0; }
  .web-address {
    position: absolute;
    left: 52px;
    bottom: 11px;
    font-size: 19px;
    color: var(--text-light);
    letter-spacing: 0.2px;
  }

  .brand-name {
    position: absolute;
    font-family: "Questrial", "Century Gothic", sans-serif;
    white-space: nowrap;
  }
  .card-front .brand-name {
    left: 90px;
    top: 205px;
    font-size: 46px;
    color: var(--accent-orange);
  }
  .card-back .brand-name {
    right: 44px;
    bottom: 55px;
    font-size: 30px;
    color: var(--mark-grey);
  }

  .details { position: absolute; left: 429px; top: 46px; }
  .person-name {
    font-family: "Poppins", "Century Gothic", sans-serif;
    font-weight: 600;
    font-size: 29px;
    line-height: 34px;
  }
  .person-role { font-size: 21px; color: var(--accent-orange); line-height: 28px; }

  .contact-list { list-style: none; }
  .contact-list li {
    display: flex;
    align-items: center;
    font-size: 18px;
    line-height: 24.5px;
    height: 24.5px;
  }
  .contact-list .icon { width: 26px; flex: none; display: flex; align-items: center; }
  .phones { margin-top: 14px; }
  .abn { margin-top: 8px; font-size: 18px; line-height: 24px; }
  .address { margin-top: 10px; font-size: 18px; line-height: 24.5px; font-style: normal; }
  .emails { margin-top: 10px; }
</style>
</head>
<body>

<section class="card card-front">
  <svg class="corner-accent" width="95" height="45" viewBox="0 0 95 45">
    <polygon points="0,0 95,0 95,45 48,45" fill="var(--accent-red)"/>
  </svg>

  <div class="brand-name">TK Servicing</div>

  <div class="details">
    <h1 class="person-name">Mr Daniel Harper</h1>
    <p class="person-role">Managing director</p>

    <ul class="contact-list phones">
      <li><span class="icon"><svg width="17" height="17" viewBox="0 0 17 17"><rect width="17" height="17" rx="3" fill="var(--accent-red)"/><path d="M5 3.5l2 2.2-1 1.3c.7 1.5 1.7 2.5 3.2 3.2l1.3-1 2.2 2-1.2 1.6C8.4 12.6 4.4 8.6 3.4 5z" fill="#fff"/></svg></span>493-127-87</li>
      <li><span class="icon"><svg width="17" height="17" viewBox="0 0 17 17"><rect width="17" height="17" rx="3" fill="var(--accent-red)"/><path d="M3.5 6.5c0-2 10-2 10 0v1.2h-2.6V6.6H6.1v1.1H3.5z M5 9h7l1 4H4z" fill="#fff"/></svg></span>493-126-88</li>
      <li><span class="icon"><svg width="17" height="17" viewBox="0 0 17 17"><rect width="17" height="17" rx="3" fill="var(--accent-red)"/><rect x="4" y="3" width="9" height="11" rx="1.5" fill="#fff"/><rect x="5.5" y="4.5" width="6" height="6.5" fill="var(--accent-red)"/></svg></span>043-891-5276</li>
    </ul>

    <p class="abn">ABN: 63 519 087 342</p>

    <address class="address">
      314 Wendale Street PO Box 7581<br>
      BRAMWELL FLATS QLD 4825
    </address>

    <ul class="contact-list emails">
      <li><span class="icon"><svg width="15" height="12" viewBox="0 0 15 12"><rect width="15" height="12" fill="var(--accent-red)"/><path d="M0 0l7.5 6.5L15 0M0 12l5.5-5M15 12l-5.5-5" stroke="#000" stroke-width="1.2" fill="none"/></svg></span>admin@tkservicing.com.au</li>
      <li><span class="icon"><svg width="15" height="12" viewBox="0 0 15 12"><rect width="15" height="12" fill="var(--accent-red)"/><path d="M0 0l7.5 6.5L15 0M0 12l5.5-5M15 12l-5.5-5" stroke="#000" stroke-width="1.2" fill="none"/></svg></span>sales@tkservicing.com.au</li>
      <li><span class="icon"><svg width="15" height="12" viewBox="0 0 15 12"><rect width="15" height="12" fill="var(--accent-red)"/><path d="M0 0l7.5 6.5L15 0M0 12l5.5-5M15 12l-5.5-5" stroke="#000" stroke-width="1.2" fill="none"/></svg></span>accounts@tkservicing.com.au</li>
      <li><span class="icon"><svg width="15" height="12" viewBox="0 0 15 12"><rect width="15" height="12" fill="var(--accent-red)"/><path d="M0 0l7.5 6.5L15 0M0 12l5.5-5M15 12l-5.5-5" stroke="#000" stroke-width="1.2" fill="none"/></svg></span>parts@tkservicing.com.au</li>
      <li><span class="icon"><svg width="15" height="12" viewBox="0 0 15 12"><rect width="15" height="12" fill="var(--accent-red)"/><path d="M0 0l7.5 6.5L15 0M0 12l5.5-5M15 12l-5.5-5" stroke="#000" stroke-width="1.2" fill="none"/></svg></span>office@tkservicing.com.au</li>
    </ul>
  </div>

  <svg class="web-band" width="335" height="48" viewBox="0 0 335 48">
    <polygon points="0,0 287,0 335,48 0,48" fill="var(--accent-red)"/>
  </svg>
  <div class="web-address">www.tkservicing.com.au</div>
</section>

<section class="card card-back">
  <div class="brand-name">TK Servicing</div>
</section>

</body>
</html>
```